Slider needed for Database Documentation Topic

We need a slider to promote a content area of a web site. I'm listing this as a poster because the posters I have seen on FrameHarbor portfolios most closely resemble the combination or art and text I am looking for.
The content area we are promoting with this graphic will clarify the design and use of a complicated database. The title of the content area is "The Kindled VQ Database" and the banner should use that title.
To 'illuminate' something means to cast light on it, and this content area will help shed light on a complicated thing – the content will use diagrams, text, and examples to clarify the database. Another meaning is that an illuminated manuscript is a manuscript brought to life with pictures, and in a way that is also what this content area will do.
One idea for the slider might be a light bulb, lamp, candle or flashlight lighting up the words "VQ Database". Another idea would be the type of illustration you see if you search for "Illuminated manuscript"
But I'm not committed to any particular idea - in the past I have been pleased to see ideas that are different than my own but accomplish the same thing, so please feel free to use your judgement or ask any questions.
In addition to the title (The Kindled VQ Database) the graphic should allow room for three smaller lines of text – the three bullet items below:
- Guide to understanding the VQ database
- Data sources, uses and relationships explained with illustrations
- New content! Customers
The last bullet item will change as the content is added.
Some particulars ...
SIZE - 600 high x 1200 wide pixels
PHOTOS vs ILLUSTRATION - I am open to either one.

```html
<!DOCTYPE html>
<html lang="en">
<head>
<meta charset="utf-8">
<title>The Kindled VQ Database – Slider</title>
<link rel="stylesheet" href="https://fonts.googleapis.com/css2?family=Carlito:wght@400;700&display=swap">
<style>
  :root {
    --page-bg: #ffffff;
    --night: #050505;
    --beam-bright: #ededed;
    --beam-mid: #8c8c8c;
    --beam-dark: #1c1c1c;
    --glow: #f6f7f7;
    --accent-yellow: #fff200;
    --title-black: #0a0a0a;
    --bullet-white: #f4f4f4;
  }
  html, body {
    margin: 0;
    padding: 0;
    width: 1200px;
    height: 1000px;
    overflow: hidden;
    background: var(--page-bg);
  }
  .canvas {
    position: relative;
    width: 1200px;
    height: 1000px;
    background: var(--page-bg);
    font-family: "Carlito", "Calibri", sans-serif;
  }
  .slider {
    position: absolute;
    left: 0;
    top: 200px;
    width: 1200px;
    height: 600px;
    overflow: hidden;
    background: var(--night);
  }
  .slider__photo {
    position: absolute;
    inset: 0;
    background:
      radial-gradient(ellipse 300px 330px at 120px 230px, var(--glow) 0%, rgba(230,232,232,0.85) 45%, transparent 85%),
      linear-gradient(180deg, var(--beam-dark) 0%, var(--beam-mid) 22%, var(--beam-bright) 44%, #b4b4b4 58%, #3a3a3a 74%, var(--night) 88%, var(--night) 100%);
  }
  .title {
    position: absolute;
    right: 0;
    margin: 0;
    line-height: 1;
    white-space: nowrap;
    text-shadow: 2px 3px 4px rgba(0,0,0,0.55);
  }
  .title__kicker {
    top: 103px;
    right: 115px;
    font-size: 95px;
    font-weight: 400;
    color: var(--accent-yellow);
  }
  .title__main {
    top: 183px;
    right: 40px;
    font-size: 145px;
    font-weight: 700;
    color: var(--title-black);
    text-shadow: 1px 2px 3px rgba(255,255,255,0.35), 3px 4px 6px rgba(0,0,0,0.5);
  }
  .highlights {
    position: absolute;
    right: 125px;
    top: 436px;
    margin: 0;
    padding: 0;
    list-style: none;
    text-align: right;
    color: var(--bullet-white);
    font-size: 29px;
    line-height: 1;
  }
  .highlights__item { height: 40px; }
  .chevrons {
    position: absolute;
    left: 1090px;
    top: 440px;
    width: 110px;
    height: 116px;
  }
  .chevrons polygon { fill: var(--accent-yellow); }
</style>
</head>
<body>
<main class="canvas">
  <section class="slider">
    <div class="slider__photo" role="img" aria-label="Photograph of a flashlight on the left casting a bright white beam of light across a dark background"></div>

    <h1 class="title title__kicker">The Kindled</h1>
    <p class="title title__main">VQ Database</p>

    <ul class="highlights">
      <li class="highlights__item">Guide to understanding the VQ database</li>
      <li class="highlights__item">Data sources, uses and relationships explained with illustrations</li>
      <li class="highlights__item">New content! Customers</li>
    </ul>

    <svg class="chevrons" viewBox="0 0 110 116" aria-hidden="true">
      <polygon points="40,0 74,0 34,58 74,116 40,116 0,58"/>
      <polygon points="86,0 110,0 72,58 110,116 86,116 46,58"/>
    </svg>
  </section>
</main>
</body>
</html>
```